Custom Framing Shop Tallpine Framing Studio

I want an eye catching graphic that will be used a s business sign on a busy road. The sign MUST communicate the type of business it is clearly to vehicles traveling at 40 mph. This is a custom picture framing business and the sign will be hanging and be approximately 32" X 48". The business name is Tallpine Framing Studio; Custom framing: by appointment and should include a whole or partial image of a picture frame as a visual que. I've included inspiration idea's, color pallets and styles that I like and a current business card for inspiration. I like the crimson font style shadowing and background colors of the attached Olans pizzeria sign. I'd prefer crimson letters. Custom Framing is the message to communicate, followed by phone number and business name. I like the idea of a shield shape with a banner since it would more eye catching, Once again the Tallpine image and name is less important than communicating what the business does. I like Crimson, grey, gold, black but am open to new ideas . I like the idea of a shield with a banner more than a rectangle, but am open to idea's

Target Market(s)

My target market is local homeowners ($700k+) who want a relationship with their framer and are willing to pay for a customized experience compared to a craft store experience. I have more female clients then men.

Industry/Entity Type

Picture Framing Art

Other font styles liked:
• Look at the attached image of a custom pizzeria sign, its kid of a custom car pinstripe font style. Script and decorative may be difficult to read while driving by but add to the elegance.

Colors

Designer to choose colors to be used in the design.

Requirements
Must have
• Clearly communicate what the business does "Custom framing" preferably with a picture frame and words
Nice to have
• incorporate a Tallpine into the graphic
Should not have
• A Tallpine image doesn't communicate what the business does to a vehicle traveling at 40 mph by the sign

```html
<!DOCTYPE html>
<html lang="en">
<head>
<meta charset="utf-8">
<title>Tallpine Framing Studio – Custom Framing Sign</title>
<link rel="stylesheet" href="https://fonts.googleapis.com/css2?family=Abril+Fatface&family=Work+Sans:wght@500;700&display=swap">
<style>
  :root {
    --paper: #f4f4f4;
    --gold: #d4bd7c;
    --olive: #7a6d45;
    --slate: #595959;
    --crimson: #862d2f;
    --oxblood: #4a1819;
    --white: #ffffff;
  }
  html, body {
    margin: 0;
    width: 1200px;
    height: 800px;
    overflow: hidden;
    background: var(--paper);
  }
  .sign { display: block; width: 1200px; height: 800px; }
  .fold { fill: var(--olive); }
  .shield-rim { fill: var(--gold); }
  .shield-field { fill: var(--slate); }
  .shield-pinline { fill: none; stroke: var(--gold); stroke-width: 17; }
  .medallion-ring { fill: var(--slate); }
  .medallion { fill: var(--gold); }
  .medallion-name {
    font-family: "Work Sans", sans-serif; font-weight: 700;
    font-size: 58px; fill: var(--crimson); letter-spacing: 4px;
  }
  .banner-edge { fill: var(--gold); }
  .banner { fill: var(--crimson); }
  .headline {
    font-family: "Abril Fatface", serif;
    font-size: 430px;
  }
  .headline-shadow { fill: var(--oxblood); }
  .headline-outline { fill: var(--white); stroke: var(--white); stroke-width: 24; stroke-linejoin: round; }
  .headline-gap { fill: var(--white); stroke: var(--crimson); stroke-width: 12; stroke-linejoin: round; }
  .headline-face { fill: var(--white); }
  .phone {
    font-family: "Work Sans", sans-serif; font-weight: 500;
    font-size: 138px; fill: var(--white); letter-spacing: 8px;
  }
  .nameplate-edge { fill: var(--gold); }
  .nameplate { fill: var(--crimson); }
  .studio-name {
    font-family: "Work Sans", sans-serif; font-weight: 700;
    font-size: 108px; fill: var(--white); letter-spacing: 3px;
  }
  .studio-tagline {
    font-family: "Work Sans", sans-serif; font-weight: 500;
    font-size: 68px; fill: var(--white); letter-spacing: 7px;
  }
</style>
</head>
<body>
<svg class="sign" viewBox="0 0 2352 1568" xmlns="http://www.w3.org/2000/svg" role="img" aria-label="Custom Framing sign for Tallpine Framing Studio">
  <!-- banner folds -->
  <polygon class="fold" points="196,282 240,243 240,950 196,912"/>
  <polygon class="fold" points="2156,282 2112,243 2112,950 2156,912"/>

  <!-- shield -->
  <path class="shield-rim" d="M240,138 H2112 V980 Q2112,1170 1925,1220 L1245,1420 Q1176,1440 1107,1420 L427,1220 Q240,1170 240,980 Z"/>
  <path class="shield-field" d="M268,166 H2084 V978 Q2084,1150 1915,1192 L1240,1392 Q1176,1410 1112,1392 L437,1192 Q268,1150 268,978 Z"/>
  <path class="shield-pinline" d="M305,203 H2047 V975 Q2047,1120 1905,1155 L1225,1355 Q1176,1370 1127,1355 L447,1155 Q305,1120 305,975 Z"/>

  <!-- medallion surround -->
  <path class="medallion-ring" d="M921,137 H1431 C1431,320 1315,450 1176,450 C1037,450 921,320 921,137 Z"/>

  <!-- banner -->
  <path class="banner-edge" d="M196,282 Q1176,440 2156,282 V912 Q1176,720 196,912 Z"/>
  <path class="banner" d="M196,320 Q1176,474 2156,320 V873 Q1176,721 196,873 Z"/>

  <!-- medallion -->
  <path class="medallion" d="M949,137 H1403 C1403,300 1300,420 1176,420 C1052,420 949,300 949,137 Z"/>
  <text class="medallion-name" x="1176" y="285" text-anchor="middle">TALLPINE</text>

  <!-- headline -->
  <g class="headline">
    <text class="headline-shadow" x="1196" y="778" text-anchor="middle" textLength="1830" lengthAdjust="spacingAndGlyphs">CUSTOM FRAMING</text>
    <text class="headline-outline" x="1176" y="752" text-anchor="middle" textLength="1830" lengthAdjust="spacingAndGlyphs">CUSTOM FRAMING</text>
    <text class="headline-gap" x="1176" y="752" text-anchor="middle" textLength="1830" lengthAdjust="spacingAndGlyphs">CUSTOM FRAMING</text>
    <text class="headline-face" x="1176" y="752" text-anchor="middle" textLength="1830" lengthAdjust="spacingAndGlyphs">CUSTOM FRAMING</text>
  </g>

  <!-- phone -->
  <text class="phone" x="1176" y="978" text-anchor="middle">(360) 555-0147</text>

  <!-- nameplate -->
  <path class="nameplate-edge" d="M779,1032 Q1176,1082 1573,1032 V1190 Q1176,1145 779,1190 Z"/>
  <path class="nameplate" d="M786,1040 Q1176,1090 1566,1040 V1182 Q1176,1138 786,1182 Z"/>
  <text class="studio-name" x="1176" y="1148" text-anchor="middle">TALLPINE</text>
  <text class="studio-tagline" x="1176" y="1232" text-anchor="middle">Framing Studio</text>
</svg>
</body>
</html>
```